Photo Storage Service - Web Application

This is web design for a simple photo storage service.
There is a web page and on the left side is a list of folders and on the right side there are photo thumbnails. By pressing a photo thumbnail, they will see the full size (it's just a link to a different page).
This project is limited only to ONE page, which is the page with the folders list and the thumbnails. However it contains some features that I will try to list here:
- Name of the service: Teso Vault
- Location of account: http://username.tesovault.example
- Folder list: Show all folders belonging to the user. Because you have to be able to drag photos to a folder, they have to be visible and cannot be hidden behind a menu item etc.
- Thumbnails with photos (in the future also videos)
- Adjusted view with smaller thumbnails and less space for folder list (so it is possible to view a larger quantity of thumbnails)- Select multiple thumbnails with rectangle- Show that a thumbnail is selected (maybe bold border?)
- Simple mobile view, but no emphasis on the mobile view in this design project.
- Drag one or more selected photos to a folder
- Delete one or more selected photos
- Drag a folder to another folder
- Rename folder
- Delete folder
- Create folder
- Show progress when deleting/moving (because it calls for every photo, so if there are 100 photos, it will delete 1 by 1 and it will take about 10 seconds - you could show progress bar or equivalent)
Background information: This is for a photo storage service NOT intended for sharing photos, but intended to indefinitely store photos and for yourself to browse your own photos.
It is a design requirement that it loads extremely fast. So we need to limit as much as possible extra graphics that cannot be done by CSS and other external libraries.
(I know this is ONLY design and nothing to do with CSS or libraries, but I can assess from the design if it might be heavy to load when implemented)
I have attached a crude screenshot of the current design, just for your understanding. It should not match this design and you are not in any way supposed to FIT your design into this same style or structure.
Target Market(s)
Consumers
Number of Pages Required
1 page

```html
<!DOCTYPE html>
<html lang="en">
<head>
<meta charset="utf-8">
<title>Teso Vault – Photos</title>
<link href="https://fonts.googleapis.com/css2?family=Poppins:wght@400;500;600;700&display=swap" rel="stylesheet">
<style>
:root{
  --blue:#1a8be4;
  --blue-dark:#0c6fcf;
  --blue-text:#1d88e5;
  --band:#eef1f5;
  --text:#4a4f57;
  --rule:#d9dce1;
  --white:#ffffff;
}
*{box-sizing:border-box;margin:0;padding:0}
html,body{width:1200px;height:949px;overflow:hidden;background:var(--white);font-family:'Poppins',sans-serif;color:var(--text)}
.app{position:relative;width:1200px;height:949px}
.topbar{position:absolute;left:0;top:0;width:1200px;height:56px;background:linear-gradient(180deg,var(--blue) 0%,var(--blue-dark) 100%)}
.brand{position:absolute;left:31px;top:13px;color:var(--white);font-weight:600;font-size:21px;letter-spacing:.2px}
.user{position:absolute;right:73px;top:19px;color:var(--white);font-size:14px;font-weight:500;letter-spacing:1.4px}
.avatar{position:absolute;left:1140px;top:16px;width:24px;height:24px;border-radius:50%;background:linear-gradient(135deg,#6b4a3c,#d9a98f);border:2px solid var(--white)}
.toolbar{position:absolute;left:0;top:56px;width:1200px;height:56px;background:var(--band)}
.selected-count{position:absolute;left:31px;top:20px;font-size:13px}
.btn-delete{position:absolute;left:934px;top:13px;width:141px;height:29px;border-radius:3px;background:var(--blue);color:var(--white);font-size:12.5px;line-height:29px;text-align:center;font-family:inherit}
.view-toggle{position:absolute;top:19px}
.view-grid{left:1100px}
.view-list{left:1143px}
.folders{position:absolute;left:31px;top:130px;width:205px;list-style:none}
.folders li{font-size:12.5px;line-height:15px;padding:7px 0 7px;border-bottom:1px solid var(--rule)}
.folders li.active{color:var(--blue-text);font-weight:600;font-size:12.5px;line-height:14px}
.folders li:last-child{border-bottom:none}
.thumb{position:absolute;display:block}
.card{position:absolute;left:534px;top:362px;width:166px;height:126px;background:var(--blue);color:var(--white);text-align:center}
.card-title{margin-top:24px;font-weight:700;font-size:16px}
.card-count{margin-top:2px;font-size:10.5px}
.card-upload{position:absolute;left:61px;top:80px;font-size:10.5px;font-weight:500}
.card-hand{position:absolute;left:130px;top:78px}
.footer-copy{position:absolute;left:36px;top:906px;font-size:10px}
.footer-more{position:absolute;left:663px;top:906px;font-size:10px;letter-spacing:.2px}
</style>
</head>
<body>
<div class="app">
  <header class="topbar">
    <div class="brand">Teso Vault</div>
    <div class="user">Lena Varga</div>
    <div class="avatar" role="img" aria-label="User profile photo"></div>
  </header>

  <div class="toolbar">
    <div class="selected-count">25 Files selected</div>
    <div class="btn-delete">Delet Selected Files</div>
    <svg class="view-toggle view-grid" width="19" height="19" viewBox="0 0 19 19" fill="#1a8be4">
      <rect x="0" y="0" width="5" height="5"/><rect x="7" y="0" width="5" height="5"/><rect x="14" y="0" width="5" height="5"/>
      <rect x="0" y="7" width="5" height="5"/><rect x="7" y="7" width="5" height="5"/><rect x="14" y="7" width="5" height="5"/>
      <rect x="0" y="14" width="5" height="5"/><rect x="7" y="14" width="5" height="5"/><rect x="14" y="14" width="5" height="5"/>
    </svg>
    <svg class="view-toggle view-list" width="20" height="19" viewBox="0 0 20 19" fill="#5f6670">
      <rect x="0" y="0" width="4" height="4"/><rect x="6" y="0" width="14" height="4"/>
      <rect x="0" y="7.5" width="4" height="4"/><rect x="6" y="7.5" width="14" height="4"/>
      <rect x="0" y="15" width="4" height="4"/><rect x="6" y="15" width="14" height="4"/>
    </svg>
  </div>

  <ul class="folders">
    <li>Inbox</li>
    <li>80s party</li>
    <li>A day in Oslo</li>
    <li>A tour of Svendborg</li>
    <li>Alicante 2017</li>
    <li>Alicante after Christmas</li>
    <li>Bandarban</li>
    <li class="active">Birds lightly garnished with monkeys and waterfals</li>
    <li>Brazil</li>
    <li>Days in Denmark - Christmas and new years</li>
    <li>Mobile Uploads</li>
    <li>Random</li>
    <li>Recently uploaded from phone</li>
    <li>Sundarban</li>
    <li>Sylhet II</li>
    <li>Tea Garden</li>
    <li>Thailand 1</li>
    <li>Thailand 2</li>
    <li>Thailand 2018</li>
    <li>Timeline Photos</li>
    <li>USA</li>
    <li>UploadBag Vancouver</li>
    <li>thumbnails</li>
    <li>videos/thumbnails</li>
  </ul>

  <main class="gallery">
    <div class="thumb" role="img" aria-label="Small bird perched on a branch" style="left:293px;top:150px;width:200px;height:135px;background:linear-gradient(135deg,#7f8a6a,#a8886e 60%,#4f5a6c)"></div>
    <div class="thumb" role="img" aria-label="Forest waterfall with hikers" style="left:293px;top:307px;width:200px;height:135px;background:linear-gradient(160deg,#3c4a30,#6a7c55 50%,#3e4d3a)"></div>
    <div class="thumb" role="img" aria-label="Black monkey walking on a branch" style="left:293px;top:464px;width:200px;height:135px;background:linear-gradient(135deg,#8a9a4e,#5d6a38 60%,#a99a6c)"></div>
    <div class="thumb" role="img" aria-label="Puffin standing on a rock" style="left:293px;top:620px;width:200px;height:237px;background:linear-gradient(180deg,#a9b9d4,#c4cde0 70%,#77808a)"></div>

    <div class="thumb" role="img" aria-label="Plate of potato fritters" style="left:516px;top:150px;width:201px;height:172px;background:linear-gradient(160deg,#e6e4e0,#d8b873 50%,#f1efec)"></div>
    <div class="thumb" role="img" aria-label="Dark waterfall scene" style="left:516px;top:346px;width:201px;height:158px;background:linear-gradient(180deg,#233038,#1b2a33)"></div>
    <div class="thumb" role="img" aria-label="Small green bird among blossoms" style="left:516px;top:526px;width:201px;height:135px;background:linear-gradient(135deg,#b9cdf1,#a8c1ef 60%,#c8d3b4)"></div>
    <div class="thumb" role="img" aria-label="Plate with sliced avocado salad" style="left:516px;top:683px;width:201px;height:173px;background:radial-gradient(circle at 50% 50%,#8aa65a 0%,#d9c9a8 45%,#f0ede8 70%)"></div>

    <div class="thumb" role="img" aria-label="Two monkeys hugging on a log" style="left:740px;top:150px;width:200px;height:295px;background:linear-gradient(160deg,#6d8d5a,#8a6c52 55%,#4a5a3e)"></div>
    <div class="thumb" role="img" aria-label="Group of macaques sitting together" style="left:740px;top:464px;width:200px;height:135px;background:linear-gradient(135deg,#6f8a68,#a49a8a 55%,#5e6a5a)"></div>
    <div class="thumb" role="img" aria-label="Fast food fries in a paper bag" style="left:740px;top:620px;width:200px;height:237px;background:linear-gradient(160deg,#4a4a4c,#c9443a 40%,#e9ddd0 75%)"></div>

    <div class="thumb" role="img" aria-label="Platter of wraps with dipping sauce" style="left:963px;top:150px;width:201px;height:135px;background:linear-gradient(135deg,#e6d6b8,#c9a36a 50%,#efe6d4)"></div>
    <div class="thumb" role="img" aria-label="Turquoise waterfall pool with swimmers" style="left:963px;top:307px;width:201px;height:291px;background:linear-gradient(180deg,#3f6e3a,#8a8a6a 40%,#3fd0d6 75%,#5fe0e0)"></div>
    <div class="thumb" role="img" aria-label="Orange bird eating an orange half" style="left:963px;top:620px;width:201px;height:235px;background:linear-gradient(135deg,#8a7a6c,#d3a06a 55%,#e87b1e)"></div>

    <div class="card">
      <div class="card-title">Nice Waterfals</div>
      <div class="card-count">Total 35 Photos</div>
      <div class="card-upload">+Upload</div>
      <svg class="card-hand" width="20" height="20" viewBox="0 0 20 20" fill="none" stroke="#ffffff" stroke-width="1.2" stroke-linecap="round" stroke-linejoin="round">
        <path d="M6 11V4.5a1.3 1.3 0 0 1 2.6 0V10"/>
        <path d="M8.6 9V7a1.3 1.3 0 0 1 2.6 0v2.5"/>
        <path d="M11.2 9.5V8a1.3 1.3 0 0 1 2.6 0v2"/>
        <path d="M13.8 10v-.5a1.3 1.3 0 0 1 2.6 0V13c0 3-2 5-5 5H10c-2 0-3-1-4-2.5L3.5 12a1.3 1.3 0 0 1 2-1.5L6 11"/>
      </svg>
    </div>
  </main>

  <footer>
    <div class="footer-copy">© 2018 TESO VAULT</div>
    <div class="footer-more">SCROL AND LOAD MORE</div>
  </footer>
</div>
</body>
</html>
```